Rack Flyer for Willowmere Dementia

We need a rack flyer design providing information on services we offer, fees and relevant contact information. Using company branding (logo, font and colours). Must be provided in a format that is easily edited for ongoing use.

For DL size (99 x 210mm)

```html
<!DOCTYPE html>
<html lang="en">
<head>
<meta charset="utf-8">
<title>Willowmere Dementia – DL Rack Flyer</title>
<link rel="stylesheet" href="https://fonts.googleapis.com/css2?family=Montserrat:ital,wght@0,400;0,500;0,700;0,800;1,700;1,800&family=Great+Vibes&display=swap">
<style>
  :root {
    --navy: #1b1c63;
    --orange: #f0a12a;
    --white: #ffffff;
    --stage: #ececec;
  }
  * { box-sizing: border-box; margin: 0; padding: 0; }
  html, body { width: 1200px; height: 909px; overflow: hidden; }
  body {
    background: var(--stage);
    font-family: "Montserrat", Arial, sans-serif;
    position: relative;
  }
  .flyer {
    position: absolute;
    top: 72px;
    width: 356px;
    height: 760px;
    background: var(--white);
    overflow: hidden;
  }
  .flyer--front { left: 182px; }
  .flyer--back { left: 662px; }

  /* Front */
  .hero-photo {
    position: absolute; left: 0; top: 0; width: 356px; height: 480px;
    background: linear-gradient(160deg, #e9eaec 0%, #cfd3d9 35%, #a9b1bd 60%, #5b5e6c 100%);
  }
  .brand-card {
    position: absolute; left: 63px; top: 421px; width: 230px; height: 91px;
    background: var(--white);
    display: flex; align-items: center; justify-content: center; gap: 10px;
    z-index: 2;
  }
  .brand-card__frame {
    position: absolute; left: 60px; top: 416px; width: 236px; height: 100px;
    border: 1px solid var(--navy); transform: rotate(-1.2deg); z-index: 1;
  }
  .brand-mark { width: 26px; height: 26px; border-radius: 50%; background: var(--orange); flex: none; }
  .brand-name {
    color: var(--navy); font-weight: 700; font-size: 20px; line-height: 1.08; letter-spacing: -0.2px;
  }
  .front-body {
    position: absolute; left: 0; top: 480px; width: 356px; height: 234px;
    background: var(--navy); color: var(--white);
    padding: 60px 20px 0 24px;
    font-size: 9.6px; line-height: 11.9px;
  }
  .front-body p { text-align: justify; }
  .front-body p + p { margin-top: 10px; }
  .front-footer { position: absolute; left: 0; top: 700px; width: 356px; height: 60px; }
  .front-footer__url {
    position: absolute; left: 0; top: 722px; width: 356px; text-align: center;
    font-size: 7.6px; color: var(--navy);
  }

  /* Back */
  .services { position: absolute; left: 0; top: 0; width: 356px; height: 328px; }
  .services__photo {
    position: absolute; inset: 0;
    background: linear-gradient(120deg, #f5f3f1 0%, #ecebe8 45%, #e5e3df 70%, #f2f1ef 100%);
  }
  .script-title {
    display: flex; align-items: center; justify-content: center; gap: 4px;
    font-family: "Great Vibes", cursive; color: var(--orange); font-weight: 400;
  }
  .script-title::before, .script-title::after {
    content: ""; height: 1px; background: var(--navy); margin-top: 14px;
  }
  .services .script-title { position: absolute; top: 30px; left: 0; width: 356px; font-size: 40px; }
  .services .script-title::before, .services .script-title::after { width: 26px; }
  .service-list {
    position: absolute; left: 52px; top: 90px; width: 280px;
    list-style: none; color: var(--navy); font-size: 9.6px; line-height: 11.4px;
  }
  .service-list li { position: relative; padding-left: 10px; margin-bottom: 6.5px; }
  .service-list li::before {
    content: ""; position: absolute; left: 0; top: 3px; width: 4px; height: 4px;
    border-right: 1.6px solid var(--orange); border-top: 1.6px solid var(--orange);
    transform: rotate(45deg);
  }
  .fees {
    position: absolute; left: 0; top: 328px; width: 356px; height: 336px;
    background: var(--navy); color: var(--white);
  }
  .fees .script-title { position: absolute; top: 18px; left: 0; width: 356px; font-size: 40px; }
  .fees .script-title::before, .fees .script-title::after { width: 24px; }
  .fee { position: absolute; width: 100px; height: 64px; }
  .fee__ring { position: absolute; left: 18px; top: 0; }
  .fee__label {
    position: absolute; left: 0; bottom: 50px; width: 100px; text-align: center;
    font-size: 6.6px; line-height: 8px;
  }
  .fee__label--narrow { left: 12px; width: 76px; }
  .fee__price {
    position: absolute; left: 0; top: 21px; width: 100px; text-align: center;
    font-weight: 800; font-size: 17px; line-height: 20px;
  }
  .fee__unit { position: absolute; left: 0; top: 41px; width: 100px; text-align: center; font-size: 4px; font-weight: 700; }
  .coverage {
    position: absolute; left: 17px; top: 229px; width: 322px;
    border: 1px solid var(--white); padding: 6px 11px 7px;
    font-size: 8.3px; line-height: 10.5px;
  }
  .fees__cta {
    position: absolute; left: 0; top: 317px; width: 356px; text-align: center;
    font-weight: 800; font-style: italic; font-size: 9.4px;
  }
  .contact { position: absolute; left: 0; top: 664px; width: 356px; height: 96px; }
  .contact__brand {
    position: absolute; left: 32px; top: 12px; display: flex; align-items: center; gap: 6px;
  }
  .contact__brand .brand-mark { width: 12px; height: 12px; }
  .contact__brand .brand-name { font-size: 10.5px; }
  .contact__details { position: absolute; right: 32px; top: 2px; text-align: right; color: var(--navy); }
  .contact__phone { font-weight: 700; font-size: 20px; line-height: 22px; letter-spacing: 0.3px; }
  .contact__line { font-size: 8.6px; line-height: 10.5px; }
  .contact__footer { position: absolute; left: 0; top: 54px; width: 356px; height: 42px; }
  .contact__tagline {
    position: absolute; left: 0; top: 78px; width: 356px; text-align: center;
    font-weight: 700; font-style: italic; font-size: 7.6px; color: var(--navy);
  }
</style>
</head>
<body>

<section class="flyer flyer--front" aria-label="Flyer front">
  <div class="hero-photo" role="img" aria-label="Photograph of a nurse comforting an elderly man seated in a chair"></div>
  <div class="brand-card__frame"></div>
  <div class="brand-card">
    <span class="brand-mark"></span>
    <span class="brand-name">Willowmere<br>Dementia</span>
  </div>
  <div class="front-body">
    <p>Navigating a diagnosis of dementia can be daunting. You likely have many questions, and it can be overwhelming trying to figure out where to turn to for answers and help. We want you to know that you are not alone in this journey.</p>
    <p>As the numbers of those living with dementia in Bermuda continue to rise placing greater demands on an already strained health care system, Willowmere's clinical and evidence based consultation services improve the safety, independence and quality of life of persons with dementia and their caregivers.<br>Our goal is to assist clients to successfully age in place at home with the support of their family caregivers to reduce the overall cost and burden of care for this vulnerable population.</p>
  </div>
  <svg class="front-footer" width="356" height="60" viewBox="0 0 356 60">
    <rect width="356" height="60" fill="#ffffff"/>
    <path d="M0 28 Q178 50 356 28 L356 60 L0 60 Z" fill="#f0a12a"/>
    <path d="M0 24 Q178 46 356 24" fill="none" stroke="#1b1c63" stroke-width="2"/>
  </svg>
  <div class="front-footer__url">www.willowmeredementia.bm</div>
</section>

<section class="flyer flyer--back" aria-label="Flyer back">
  <div class="services">
    <div class="services__photo" role="img" aria-label="Faded photograph of a carer with an elderly woman at home"></div>
    <h2 class="script-title">Services Offered</h2>
    <ul class="service-list">
      <li>Comprehensive Dementia Assessment</li>
      <li>Cognitive/Perceptual Screening</li>
      <li>Home Safety Audit (Home modifications and adaptive equipment aids)</li>
      <li>Caregiver Education &amp; Support</li>
      <li>Falls Prevention Strategies</li>
      <li>Personalised Care Planning</li>
      <li>Preparation for future disease progression</li>
      <li>Case Management Support</li>
      <li>Check-in/monitoring visits for clients with limited social support</li>
      <li>Cognitive Stimulation Therapy (group program for individuals with mild-moderate stage dementia)</li>
    </ul>
  </div>

  <div class="fees">
    <h2 class="script-title">Service Fees</h2>

    <div class="fee" style="left:19px;top:84px">
      <svg class="fee__ring" width="64" height="64" viewBox="0 0 64 64"><path d="M7.4 14.8 A30 30 0 1 0 56.6 14.8" fill="none" stroke="#f0a12a" stroke-width="2.2"/></svg>
      <div class="fee__label">Initial Consultation</div>
      <div class="fee__price">$180</div>
    </div>
    <div class="fee" style="left:120px;top:84px">
      <svg class="fee__ring" width="64" height="64" viewBox="0 0 64 64"><path d="M7.4 14.8 A30 30 0 1 0 56.6 14.8" fill="none" stroke="#f0a12a" stroke-width="2.2"/></svg>
      <div class="fee__label">Comprehensive Dementia Assessment</div>
      <div class="fee__price">$395</div>
    </div>
    <div class="fee" style="left:224px;top:84px">
      <svg class="fee__ring" width="64" height="64" viewBox="0 0 64 64"><path d="M7.4 14.8 A30 30 0 1 0 56.6 14.8" fill="none" stroke="#f0a12a" stroke-width="2.2"/></svg>
      <div class="fee__label">Comprehensive Dementia Assessment &amp; ongoing case management services</div>
      <div class="fee__price">$720</div>
    </div>
    <div class="fee" style="left:74px;top:150px">
      <svg class="fee__ring" width="64" height="64" viewBox="0 0 64 64"><path d="M7.4 14.8 A30 30 0 1 0 56.6 14.8" fill="none" stroke="#f0a12a" stroke-width="2.2"/></svg>
      <div class="fee__label fee__label--narrow">Monthly check in monitoring visits</div>
      <div class="fee__price">$180</div>
    </div>
    <div class="fee" style="left:171px;top:150px">
      <svg class="fee__ring" width="64" height="64" viewBox="0 0 64 64"><path d="M7.4 14.8 A30 30 0 1 0 56.6 14.8" fill="none" stroke="#f0a12a" stroke-width="2.2"/></svg>
      <div class="fee__label fee__label--narrow">Cognitive Stimulation Therapy</div>
      <div class="fee__price">$500</div>
      <div class="fee__unit">per term</div>
    </div>

    <div class="coverage">We are pleased to share that services offered by Willowmere Dementia are currently covered under Harbourline and Keystone health insurance plans. We also have availability of funding support for those in financial need who are unable to afford co-pay, enabling equitable access to these essential care and support services regardless of financial means.</div>
    <p class="fees__cta">Please feel free to reach out for further information.</p>
  </div>

  <div class="contact">
    <div class="contact__brand">
      <span class="brand-mark"></span>
      <span class="brand-name">Willowmere<br>Dementia</span>
    </div>
    <div class="contact__details">
      <div class="contact__phone">(441) 555 0148</div>
      <div class="contact__line">www.willowmeredementia.bm</div>
      <div class="contact__line">hello@willowmeredementia.bm</div>
    </div>
    <svg class="contact__footer" width="356" height="42" viewBox="0 0 356 42">
      <path d="M0 4 Q178 20 356 4 L356 42 L0 42 Z" fill="#f0a12a"/>
      <path d="M0 2 Q178 18 356 2" fill="none" stroke="#1b1c63" stroke-width="2.4"/>
    </svg>
    <div class="contact__tagline">Navigating Dementia Together</div>
  </div>
</section>

</body>
</html>
```